Business Card Design Project

Company name will be Tolvan Crest (named after my black lab and his fraying muzzle) Business is in the body armor, Security product industry servicing the state, local, and federal law enforcement markets. I want a more formal and serious logo for both business cards and letterhead

```html
<!DOCTYPE html>
<html lang="en">
<head>
<meta charset="utf-8">
<title>Tolvan Crest – Business Card</title>
<link rel="stylesheet" href="https://fonts.googleapis.com/css2?family=Source+Sans+3:wght@300;400;700;900&display=swap">
<style>
  :root {
    --card-bg: #333333;
    --ink: #ffffff;
    --ink-soft: #f2f2f2;
    --mark-fill: #5a5a5a;
  }
  html, body {
    margin: 0;
    padding: 0;
    width: 777px;
    height: 1200px;
    overflow: hidden;
    background: var(--card-bg);
  }
  .card {
    position: relative;
    width: 777px;
    height: 1200px;
    background: var(--card-bg);
    color: var(--ink);
    font-family: "Source Sans 3", "Myriad Pro", Arial, sans-serif;
    text-align: center;
  }
  .crest-mark {
    position: absolute;
    top: 90px;
    left: 238px;
    width: 300px;
    height: 300px;
    border-radius: 50%;
    background: var(--mark-fill);
  }
  .brand-name {
    position: absolute;
    top: 408px;
    left: 0;
    width: 100%;
    margin: 0;
    font-weight: 900;
    font-size: 142px;
    line-height: 0.93;
    letter-spacing: -2px;
    color: var(--ink);
  }
  .brand-name span { display: block; }
  .tagline {
    position: absolute;
    top: 716px;
    left: 0;
    width: 100%;
    margin: 0;
    font-weight: 900;
    font-size: 18px;
    letter-spacing: 14px;
    color: var(--ink);
  }
  .tagline .divider {
    display: inline-block;
    width: 3px;
    height: 14px;
    background: var(--ink);
    margin: 0 40px 0 26px;
    vertical-align: -1px;
  }
  .contact {
    position: absolute;
    top: 868px;
    left: 0;
    width: 100%;
  }
  .person-name {
    margin: 0;
    font-weight: 700;
    font-size: 38px;
    line-height: 1.1;
    letter-spacing: -0.5px;
  }
  .person-title {
    margin: 2px 0 0;
    font-weight: 300;
    font-size: 30px;
    line-height: 1.2;
    color: var(--ink-soft);
  }
  .address {
    margin: 34px 0 0;
    font-weight: 300;
    font-size: 30px;
    line-height: 1.45;
    font-style: normal;
    color: var(--ink-soft);
  }
  .reach {
    margin: 14px 0 0;
    font-weight: 700;
    font-size: 33px;
    letter-spacing: -0.3px;
  }
  .reach .divider {
    display: inline-block;
    width: 3px;
    height: 36px;
    background: var(--ink);
    margin: 0 12px;
    vertical-align: -5px;
  }
</style>
</head>
<body>
  <main class="card">
    <div class="crest-mark" aria-hidden="true"></div>
    <h1 class="brand-name"><span>Tolvan</span><span>Crest</span></h1>
    <p class="tagline">security<span class="divider"></span>body armor</p>

    <section class="contact">
      <p class="person-name">Rowan Hale</p>
      <p class="person-title">Manufacturers Rep. Principal</p>
      <address class="address">1470 Harbor Lane North<br>SEABROOK SHORES, FL 32099</address>
      <p class="reach">f. 555-014-2273<span class="divider"></span>rhaletc7@mailbox.com</p>
    </section>
  </main>
</body>
</html>
```